Cordial Keys

We teach men how to be successful with women.

We will be putting an Vidhostly on the page.

We want to push men to take our 12 month learning program.

Open to ideas and layouts. The website will also be a landing page for our TV campaign.

Cordial keys is a company that will be marketing as an infomercial on late night television and via the internet. 

We will be selling a 12 month program for $997 (paid monthly). It will teach men how to get the woman of their dreams and how attraction is not a choice.
We have systematically developed a program for helping men attract women. 
We do have some competitors but they in the pickup commuinity (Hob Board, Greg Tolliver and Quillon Methods are all competitors.
Our website name is cordialkeys.com.au.
We will be having an vidhostly.com.au on our website to aid the process on making the sale.

The program will be an e-learning program that will be purchased over 12 months.

We also will be selling boot camps in which guys go for a week at a time and train to refine their skills.

Tv

```html
<!DOCTYPE html>
<html lang="en">
<head>
<meta charset="utf-8">
<title>Cordial Keys</title>
<link href="https://fonts.googleapis.com/css2?family=Cabin:wght@400;500;600&family=Montserrat:wght@800;900&family=Oswald:wght@600&display=swap" rel="stylesheet">
<style>
:root{
  --black:#000;
  --red:#d90000;
  --red-dark:#b00000;
  --blue:#1a7fd0;
  --page:#f4f4f4;
  --box:#e4e4e4;
  --box-line:#cfcfcf;
  --text:#555;
  --white:#fff;
  --sky-1:#e9f2fb;
  --sky-2:#5aa6e6;
}
*{box-sizing:border-box;margin:0;padding:0}
html,body{width:1200px;height:912px;overflow:hidden}
body{position:relative;background:var(--page);font-family:"Cabin",sans-serif;color:var(--text)}
.site-header{position:absolute;left:0;top:0;width:1200px;height:93px;background:var(--black)}
.site-header::after{content:"";position:absolute;left:0;bottom:-5px;width:100%;height:5px;
  background:linear-gradient(135deg,var(--black) 3.5px,transparent 0),linear-gradient(225deg,var(--black) 3.5px,transparent 0);
  background-size:7px 7px;background-position:left top;z-index:3}
.brand{position:absolute;left:182px;top:22px;color:var(--red);font:600 34px/1 "Cabin",sans-serif;letter-spacing:.5px}
.main-nav{position:absolute;left:444px;top:36px;display:flex;align-items:center;gap:0}
.main-nav a{color:var(--white);text-decoration:none;font:400 14.5px/27px "Cabin",sans-serif;margin-right:11px}
.main-nav a.active{background:linear-gradient(#fff,#e6e6e6);color:var(--red);padding:0 9px;border-radius:3px;margin-right:6px;position:relative}
.main-nav a.active::after{content:"";position:absolute;left:50%;bottom:-5px;margin-left:-5px;border:5px solid transparent;border-bottom:0;border-top-color:#e6e6e6}
.hero{position:absolute;left:0;top:93px;width:1200px;height:360px;
  background:radial-gradient(ellipse at 30% 20%,var(--white) 0,var(--sky-1) 30%,transparent 60%),linear-gradient(180deg,#d8e9f8 0,var(--sky-2) 100%)}
.hero-photo{position:absolute;left:257px;top:44px;width:403px;height:316px;background:linear-gradient(180deg,#b6c8de,#6a79a8 70%,#4c5d8e);opacity:.75}
.hero-pitch{position:absolute;left:742px;top:68px;width:240px;text-align:center}
.hero-pitch .big{display:block;font:900 72px/1 "Montserrat",sans-serif;color:var(--red);letter-spacing:1px}
.hero-pitch .mid{display:block;font:800 25px/1 "Montserrat",sans-serif;color:var(--black);margin-top:6px}
.hero-pitch .big.dark{color:var(--black);font-size:58px;margin-top:6px}
.cta{display:block;margin-top:13px;width:237px;height:58px;border-radius:4px;background:linear-gradient(#f00,var(--red-dark));
  color:var(--white);font:600 24px/58px "Oswald",sans-serif;text-decoration:none;box-shadow:0 1px 2px rgba(0,0,0,.3)}
.features{position:absolute;left:190px;top:482px;width:620px;display:flex}
.feature{width:202px;padding:0 8px;text-align:center;position:relative}
.feature+.feature{border-left:1px solid #e4e4e4}
.feature:nth-child(2){width:216px}
.feature-icon{width:53px;height:53px;margin:0 auto}
.feature h2{color:var(--blue);font:400 16px/19px "Cabin",sans-serif;margin-top:18px}
.feature p{text-align:left;font:400 12px/15.4px "Cabin",sans-serif;margin:12px 0 0 8px;height:115px}
.stories{position:absolute;left:189px;top:678px;width:615px}
.stories h2{color:var(--red);font:400 15.5px/20px "Cabin",sans-serif;margin-left:1px}
.story{margin-top:7px;background:var(--box);border:1px solid var(--box-line);border-radius:3px;padding:13px 13px 10px}
.story p{font:400 11.5px/15.5px "Cabin",sans-serif;color:#444}
.story cite{display:block;font:400 11.5px/15px "Cabin",sans-serif;font-style:normal;color:#333;margin-top:9px}
.presenter{position:absolute;left:844px;top:561px;width:146px;height:269px;background:linear-gradient(180deg,#d9d2cc 0,#8591ad 35%,#5d6a8d 100%);border-radius:50px 50px 0 0}
.site-footer{position:absolute;left:0;top:830px;width:1200px;height:82px;background:var(--red)}
.site-footer::before{content:"";position:absolute;left:0;top:-5px;width:100%;height:5px;
  background:linear-gradient(45deg,var(--red) 3.5px,transparent 0),linear-gradient(-45deg,var(--red) 3.5px,transparent 0);
  background-size:7px 7px;background-position:left bottom}
.footer-nav{position:absolute;left:188px;top:17px;display:flex;gap:15px}
.footer-nav a{color:var(--white);text-decoration:none;font:400 13.5px/18px "Cabin",sans-serif}
.copyright{position:absolute;left:188px;top:42px;color:var(--white);font:400 11.5px/14px "Cabin",sans-serif}
.social{position:absolute;left:880px;top:23px;display:flex;gap:6px}
.social span{width:37px;height:37px;background:linear-gradient(#fff,#ddd);border-radius:2px}
</style>
</head>
<body>
<header class="site-header">
  <div class="brand">Cordial Keys</div>
  <nav class="main-nav">
    <a class="active" href="#">Home</a>
    <a href="#">About us</a>
    <a href="#">Bootcamp</a>
    <a href="#">Learning Program</a>
    <a href="#">Success Stories</a>
    <a href="#">FAQ</a>
    <a href="#">Contact us</a>
  </nav>
</header>

<section class="hero">
  <div class="hero-photo" role="img" aria-label="A smiling woman standing beside a sad man holding a broken paper heart"></div>
  <div class="hero-pitch">
    <span class="big">DON’T</span>
    <span class="mid">LET THIS HAPPEN</span>
    <span class="big dark">TO YOU!</span>
    <a class="cta" href="#">MAKE A CHANGE NOW!</a>
  </div>
</section>

<section class="features">
  <div class="feature">
    <svg class="feature-icon" viewBox="0 0 53 53"><circle cx="26.5" cy="26.5" r="25.5" fill="#222" stroke="#666"/><path d="M20 15 L38 26.5 L20 38Z" fill="#ddd"/></svg>
    <h2>Make a Change<br>Now</h2>
    <p>Get the Woman of your Dream. Take our 12 month Learning Program. It's Simple</p>
  </div>
  <div class="feature">
    <svg class="feature-icon" viewBox="0 0 53 53"><circle cx="26.5" cy="26.5" r="25.5" fill="#222" stroke="#666"/><path d="M26.5 16 L39 35 H14Z" fill="#ddd"/><path d="M26.5 27 L30 35 H23Z" fill="#222"/></svg>
    <h2>Join Our<br>Bootcamp Now</h2>
    <p>Go for a week training &amp; refine your skills. We will train you, how to Get the woman of your Dreams</p>
  </div>
  <div class="feature">
    <svg class="feature-icon" viewBox="0 0 53 53"><circle cx="26.5" cy="26.5" r="25.5" fill="#222" stroke="#666"/><text x="26.5" y="36" text-anchor="middle" font-family="Montserrat,sans-serif" font-weight="900" font-size="28" fill="#ddd">?</text></svg>
    <h2>Frequently Asked<br>Questions</h2>
    <p>Nulla vitae imperdiet elit. Quisque vehicula, nulla sit amet ultrices molestie, purus tortor consequat magna, et eleifend elit quam</p>
  </div>
</section>

<section class="stories">
  <h2>Success Stories</h2>
  <blockquote class="story">
    <p>“Praesent sed magna augue, at pulvinar lorem. Ut vulputate mauris ac velit fermentum condimentum. Curabitur vel justo tellus, ut blandit erat. Vestibulum ante ipsum primis in faucibus orci luctus et ultrices posuere cubilia Curae; Aenean libero massa, lacinia elementum pulvinar et, fermentum in odio. Quisque eleifend quam acopi”</p>
    <cite>Nolan Brecker</cite>
  </blockquote>
</section>

<div class="presenter" role="img" aria-label="Video presenter, a woman in a grey blazer standing with hands clasped"></div>

<footer class="site-footer">
  <nav class="footer-nav">
    <a href="#">Home</a>
    <a href="#">About us</a>
    <a href="#">Bootcamp</a>
    <a href="#">Learning Program</a>
    <a href="#">FAQ</a>
    <a href="#">Success Stories</a>
    <a href="#">Contact us</a>
  </nav>
  <p class="copyright">Copyright © 2013 cordialkeys.com.au. All rights reserved</p>
  <div class="social" aria-label="Social links"><span></span><span></span><span></span></div>
</footer>
</body>
</html>
```